Etiketten-Design für Fruchtsäfte
Zielgruppe
Wir sind ein Obstbaubetrieb und suchen für unsere Fruchtsäfte ein neues modernes Etikett
Aufgabenstellung
Wir benötigen ein Etikett für unseren Pfirsichnektar, Kirschennektar, Marillennektar und Traubensaft.
Es kann sich hierbei um das selbe Muster handeln, nur bei der Bezeichnung sollte Wendlingers Marillennektar stehen.
Als Muster was wir uns vorstellen würden füge ich zwei Bilder von einem Obstbaukollegen hinzu.Wir sind aber für alles offen. Außerdem anbei unser Logo, wo nicht Obstbau Wendlinger stehen muss sondern vielleicht nur die Frucht in der Mitte und dann eben Wendlingers Traubensaft usw. Und auch anbei unsere aktuellen Etiketten. Vom Format her und Beschriftung sollte es ähnlich wie unsere alten Etiketten sein. Vielleicht nur etwas schmaler.

```html
<!DOCTYPE html>
<html lang="de">
<head>
<meta charset="utf-8">
<title>Etikett – Obstbau Wendlinger</title>
<link rel="stylesheet" href="https://fonts.googleapis.com/css2?family=Montserrat:wght@400;500;700&display=swap">
<style>
  :root {
    --blush: #f6b3ae;
    --rose-band: #ee8e97;
    --terracotta: #db7b73;
    --paper: #ffffff;
    --ink: #111111;
    --peach-light: #f7b9b4;
    --peach-mid: #f3a4ae;
    --peach-deep: #e88a92;
  }
  html, body {
    margin: 0;
    padding: 0;
    overflow: hidden;
    background: #eeeeee;
  }
  .label {
    position: relative;
    width: 848px;
    height: 1200px;
    overflow: hidden;
    font-family: "Montserrat", Arial, sans-serif;
    color: var(--ink);
    background: var(--blush);
  }
  .label-backdrop {
    position: absolute;
    inset: 0;
  }
  .shelf-note {
    position: absolute;
    left: 157px;
    top: 46px;
    margin: 0;
    font-size: 22px;
    line-height: 30px;
    font-weight: 500;
  }
  .ingredients {
    position: absolute;
    left: 157px;
    top: 240px;
    width: 520px;
  }
  .ingredients h2 {
    margin: 0;
    font-size: 30px;
    line-height: 38px;
    font-weight: 700;
  }
  .ingredients p {
    margin: 0 0 12px;
    font-size: 30px;
    line-height: 40px;
    font-weight: 400;
  }
  .producer {
    position: absolute;
    left: 162px;
    top: 578px;
    font-size: 19px;
    line-height: 24px;
  }
  .producer strong {
    display: block;
    font-size: 20px;
    font-weight: 700;
  }
  .contact-card {
    position: absolute;
    left: 50px;
    top: 1022px;
    width: 462px;
    height: 148px;
    background: var(--paper);
    border-radius: 14px;
    box-sizing: border-box;
    padding: 11px 0 0 10px;
  }
  .contact-row {
    display: flex;
    align-items: center;
    height: 47px;
    font-size: 22px;
    font-weight: 500;
  }
  .contact-icon {
    width: 30px;
    height: 30px;
    margin-right: 20px;
    flex: none;
  }
</style>
</head>
<body>
<div class="label">
  <svg class="label-backdrop" width="848" height="1200" viewBox="0 0 848 1200">
    <defs>
      <radialGradient id="peach-tone" cx="40%" cy="40%" r="65%">
        <stop offset="0" stop-color="var(--peach-light)"/>
        <stop offset="0.7" stop-color="var(--peach-mid)"/>
        <stop offset="1" stop-color="var(--peach-deep)"/>
      </radialGradient>
    </defs>
    <path class="rose-band" fill="var(--rose-band)"
      d="M0 605 L111 612 L111 1200 L0 1200 Z M737 582 C780 565 815 555 848 540 L848 1200 L737 1200 Z"/>
    <rect class="text-panel" x="111" y="0" width="626" height="860" fill="var(--paper)"/>
    <path class="ground" fill="var(--terracotta)"
      d="M0 688 C150 676 300 712 385 770 C450 812 520 830 600 805 C700 772 780 700 848 668 L848 1200 L0 1200 Z"/>
    <g role="img" aria-label="Illustration: kleiner Pfirsich mit Blättern links">
      <ellipse cx="118" cy="862" rx="70" ry="10" fill="#c4665f" opacity="0.6"/>
      <circle cx="118" cy="796" r="72" fill="url(#peach-tone)"/>
    </g>
    <g role="img" aria-label="Illustration: Pfirsich mit Stiel rechts">
      <ellipse cx="718" cy="720" rx="102" ry="98" fill="url(#peach-tone)"/>
    </g>
    <g role="img" aria-label="Illustration: großer Pfirsich mit Blättern im Vordergrund">
      <ellipse cx="570" cy="1175" rx="150" ry="22" fill="#c4665f" opacity="0.6"/>
      <ellipse cx="560" cy="1000" rx="158" ry="170" fill="url(#peach-tone)"/>
    </g>
  </svg>

  <p class="shelf-note">Durch Erhitzen haltbar gemacht<br>Mindestens Haltbar bis: siehe Verschluss</p>

  <section class="ingredients">
    <h2>Zutaten:</h2>
    <p>Wasser, XXXXXXX,<br>Weichselmark, Zucker.</p>
    <h2>Säuerungsmittel:</h2>
    <p>Zitronensäure</p>
    <h2>Antioxidationsmittel:</h2>
    <p>Ascorbinsäure</p>
  </section>

  <address class="producer" style="font-style:normal">
    <strong>Obstbau Wendlinger</strong>
    Lindenweg 14<br>
    AT - 7061 Obersdorf
  </address>

  <div class="contact-card">
    <div class="contact-row">
      <svg class="contact-icon" viewBox="0 0 30 30" aria-hidden="true">
        <circle cx="15" cy="15" r="15" fill="var(--ink)"/>
        <path fill="#fff" d="M10 7.5c.8-.5 1.6-.3 2 .4l1.6 2.7c.4.7.2 1.4-.4 1.9l-1 .8c.8 1.8 2.2 3.3 4 4.2l.9-1c.5-.6 1.3-.7 1.9-.3l2.6 1.7c.7.4.8 1.3.3 2l-1 1.3c-.6.8-1.7 1.1-2.7.8-4.4-1.5-7.6-4.8-9-9.2-.3-1 0-2 .8-2.6z"/>
      </svg>
      +43 66012457830
    </div>
    <div class="contact-row">
      <svg class="contact-icon" viewBox="0 0 30 30" aria-hidden="true">
        <circle cx="15" cy="15" r="15" fill="var(--ink)"/>
        <rect x="7.5" y="10" width="15" height="10.5" rx="1.2" fill="#fff"/>
        <path d="M8 10.8l7 5.2 7-5.2" fill="none" stroke="var(--ink)" stroke-width="1.4"/>
      </svg>
      obstbau.wendlinger@postfach.at
    </div>
    <div class="contact-row">
      <svg class="contact-icon" viewBox="0 0 30 30" aria-hidden="true">
        <circle cx="15" cy="15" r="15" fill="var(--ink)"/>
        <g fill="none" stroke="#fff" stroke-width="1.3">
          <circle cx="15" cy="15" r="7.5"/>
          <ellipse cx="15" cy="15" rx="3.2" ry="7.5"/>
          <path d="M7.5 15h15M8.5 11.2h13M8.5 18.8h13"/>
        </g>
      </svg>
      www.obstbau-wendlinger.at
    </div>
  </div>
</div>
</body>
</html>
```